Flyer für Restaurant
Zielgruppe
Deutsche Küche mit Südafrikanischen Flair
Restaurant was auch Feierlichkeiten anbieten
Jung und Alt
Aufgabenstellung
Farbe : Wein rot und grau
Erleben Sie bei uns einen Abend mit vielfältiger oder deutscher Küche und all ihren Rafinessen. Sehen Sie sich unser Restaurant Gasthaus Dornbeck an, das mit einer Vielzahl an schmackhaften Speisen begeistert und noch dazu urgemütlich ist. Absolute Erholung bietet an warmen Tagen unser toller Außenbereich.
Parken können Sie ganz einfach vor dem Restaurant auf unseren kostenlosen Parkplätzen. Uns ist es wichtig, dass wir alle Menschen willkommen heißen können. Aus diesem Grund haben wir einen barrierefreien Zugang. Gerne nehmen wir Ihre Reservierung entgegen. Freuen Sie sich auf einen wundervollen Aufenthalt mit idyllischem Flair in unserem Restaurant. Darüber hinaus können Sie uns einfach per Telefon unter +4957218640 kontaktieren.
Flyer um in Briefkasten zu werfen

```html
<!DOCTYPE html>
<html lang="de">
<head>
<meta charset="utf-8">
<title>Gasthaus Dornbeck – Flyer</title>
<link href="https://fonts.googleapis.com/css2?family=Crimson+Text:ital,wght@0,600;0,700;1,600&family=Fira+Sans:ital,wght@0,400;0,500;0,600;1,400;1,600;1,700&display=swap" rel="stylesheet">
<style>
  :root{
    --wine:#741c24;
    --grey:#5f5f61;
    --grey-box:#a7a9ab;
    --grey-line:#b3b5b6;
    --paper:#efefef;
    --bg:#bab8ba;
    --white:#ffffff;
  }
  *{box-sizing:border-box;margin:0;padding:0}
  html,body{width:1200px;height:1130px;overflow:hidden;background:var(--bg)}
  body{position:relative;font-family:"Fira Sans",sans-serif}
  .flyer{position:absolute;top:246px;width:456px;height:649px;overflow:hidden;box-shadow:0 2px 6px rgba(0,0,0,.25)}
  .flyer--front{left:120px;background:var(--wine);color:var(--white)}
  .flyer--back{left:628px;background:var(--paper)}
  .abs{position:absolute}
  svg.abs{display:block}

  /* Vorderseite */
  .headline{font-family:"Crimson Text",serif;font-weight:700;line-height:1;white-space:nowrap}
  .headline em{font-style:italic;font-weight:600}
  .tagline{left:69px;top:434px;font-size:15px;letter-spacing:2.6px;line-height:26px;font-weight:500}
  .intro{left:68px;top:530px;font-size:11px;font-style:italic;letter-spacing:1px;line-height:15.5px}
  .front-phone{left:68px;top:600px;font-size:15px;font-weight:500;letter-spacing:3px;display:flex;align-items:center;gap:8px}
  .house-photo{left:279px;top:471px;width:147px;height:146px;border:2px solid var(--white);border-radius:10px;background:linear-gradient(180deg,#3e6fb4 0%,#e9dfc6 35%,#cfc5ad 70%,#8a8a86 100%);box-shadow:2px 3px 6px rgba(0,0,0,.35)}
  .cutlery{left:300px;top:300px;width:150px;height:170px;background:radial-gradient(ellipse,rgba(255,255,255,.1),rgba(255,255,255,0) 70%)}

  /* Rückseite */
  .feier-title{left:0;width:100%;text-align:center;font-family:"Crimson Text",serif;font-weight:700;line-height:1}
  .feier-title .accent{color:var(--wine)}
  .occasions{left:50px;top:272px;list-style:none;color:var(--grey);font-size:13px;font-weight:500}
  .occasions li{display:flex;align-items:center;gap:14px;height:36px}
  .occasions li:last-child{height:44px;line-height:20px}
  .hours{left:237px;top:278px;width:195px;height:119px;background:var(--grey-box);border:2px solid var(--white);border-radius:10px;box-shadow:2px 3px 6px rgba(0,0,0,.25);color:#55575a;padding:15px 18px;font-size:8.5px}
  .hours .times{font-size:11px;font-weight:700;font-style:italic;line-height:20px;margin:7px 0 5px}
  .perks-title{left:53px;top:410px;color:var(--wine);font-size:13px;font-weight:600}
  .perks{left:53px;top:440px;color:var(--grey);font-size:11.5px;font-weight:500;list-style:none}
  .perks li{height:21.5px;position:relative}
  .perks li::before{content:"";position:absolute;left:-11px;top:6px;width:3px;height:3px;border-radius:50%;background:var(--grey)}
  .reserve{left:0;width:100%;text-align:center;color:var(--white);font-style:italic;line-height:1.1}
</style>
</head>
<body>

<section class="flyer flyer--front">
  <svg class="abs" style="left:0;top:0" width="456" height="262" viewBox="0 0 456 262" role="img" aria-label="Foto: paniertes Schnitzel mit Pommes frites und Zitrone auf einem Teller">
    <defs>
      <linearGradient id="dish" x1="0" y1="0" x2="1" y2="1">
        <stop offset="0" stop-color="#d9a44a"/>
        <stop offset=".5" stop-color="#c98a3a"/>
        <stop offset="1" stop-color="#e8bf52"/>
      </linearGradient>
    </defs>
    <path d="M0 0H456V210Q330 262 200 256Q80 250 0 180Z" fill="url(#dish)"/>
    <path d="M0 180Q80 250 200 256Q330 262 456 210" fill="none" stroke="#ece4da" stroke-width="8"/>
  </svg>
  <div class="abs cutlery" role="img" aria-label="Dezente Besteck-Silhouette als Hintergrundmotiv"></div>

  <div class="abs headline" style="left:31px;top:272px;font-size:49px">Willkommen <em style="font-size:35px;margin-left:8px">im</em></div>
  <div class="abs headline" style="left:109px;top:328px;font-size:52px">Gasthaus</div>
  <div class="abs headline" style="left:74px;top:373px;font-size:52px">Dornbeck</div>

  <p class="abs tagline">wo deutsche Küche<br>auf südafrikanisches<br>Flair trifft.</p>
  <p class="abs intro">Unser Haus bietet für Jung<br>&amp; Alt ein entspanntes Ambiente<br>zum Wohlfühlen.</p>
  <div class="abs front-phone">
    <svg width="15" height="15" viewBox="0 0 24 24"><path fill="#fff" d="M6.6 10.8a15.1 15.1 0 0 0 6.6 6.6l2.2-2.2a1 1 0 0 1 1-.25 11.4 11.4 0 0 0 3.6.57 1 1 0 0 1 1 1V20a1 1 0 0 1-1 1A17 17 0 0 1 3 4a1 1 0 0 1 1-1h3.5a1 1 0 0 1 1 1c0 1.25.2 2.45.57 3.6a1 1 0 0 1-.25 1z"/></svg>
    <span>05721 / 8640</span>
  </div>
  <div class="abs house-photo" role="img" aria-label="Foto: Außenansicht des Gasthauses mit Sonnenschirmen auf der Terrasse"></div>
</section>

<section class="flyer flyer--back">
  <div class="abs" style="left:0;top:0;width:456px;height:215px;background:linear-gradient(100deg,#5d5a66 0%,#8b7f8c 35%,#c9c6cc 70%,#a5a3a8 100%)" role="img" aria-label="Foto: festlich gedeckte Tafel mit Tulpen und Servietten"></div>
  <svg class="abs" style="left:0;top:0" width="456" height="230" viewBox="0 0 456 230">
    <path d="M0 190Q228 20 456 190V230H0Z" fill="var(--grey-line)"/>
    <path d="M0 175Q228 58 456 175V230H0Z" fill="var(--wine)"/>
    <path d="M0 205Q228 43 456 205V230H0Z" fill="var(--white)"/>
    <path d="M0 212Q228 44 456 212V230H0Z" fill="var(--paper)"/>
  </svg>

  <div class="abs feier-title" style="top:174px;font-size:36px"><span class="accent">Ihre FEIER</span> <span style="color:var(--grey)">im</span></div>
  <div class="abs feier-title" style="top:214px;font-size:37px;color:var(--grey)">Gasthaus Dornbeck</div>

  <ul class="abs occasions">
    <li>
      <svg width="28" height="26" viewBox="0 0 28 26" fill="none" stroke="#5f5f61" stroke-width="1.6"><path d="M14 2v5M5 12h18v4H5zM3 16h22v7H3zM6 12V9h16v3"/><path d="M1 24h26"/></svg>
      Geburtstage
    </li>
    <li>
      <svg width="28" height="28" viewBox="0 0 28 28" fill="none" stroke="#5f5f61" stroke-width="1.6"><path d="M6 8h7l-1 7a3 3 0 0 1-5 0zM9.5 17v8M6 25h7M15 8h7l-1 7a3 3 0 0 1-5 0zM18.5 17v8M15 25h7M13 2l1 3M8 3l2 2M20 3l-2 2"/></svg>
      Jubiläen
    </li>
    <li>
      <svg width="28" height="24" viewBox="0 0 28 24" fill="#5f5f61"><circle cx="5" cy="6" r="2.5"/><circle cx="14" cy="5" r="2.5"/><circle cx="23" cy="6" r="2.5"/><rect x="3" y="10" width="4" height="12" rx="1"/><rect x="12" y="9" width="4" height="13" rx="1"/><rect x="21" y="10" width="4" height="12" rx="1"/></svg>
      <span>Vereinsabende &amp;<br>Firmenfeiern</span>
    </li>
  </ul>

  <div class="abs hours">
    <p>Wir haben 5 Tagen&nbsp; die Woche geöffnet:</p>
    <p class="times">11.00-14.30 Uhr und von<br>17.00-20.00 Uhr geöffnet.</p>
    <p>Ruhetage sind Dienstag und Mittwoch.</p>
  </div>

  <p class="abs perks-title">Besonders angenehm für Sie:</p>
  <ul class="abs perks">
    <li>gemütliche Gasträume &amp; idyllischer Außenbereich</li>
    <li>barrierefreier Zugang</li>
    <li>kostenlose Parkplätze direkt vor dem Haus</li>
  </ul>

  <svg class="abs" style="left:0;top:500px" width="456" height="149" viewBox="0 0 456 149">
    <path d="M0 60Q228 -30 456 60V149H0Z" fill="var(--grey-line)"/>
    <path d="M0 66Q228 -14 456 68V149H0Z" fill="var(--white)"/>
    <path d="M0 72Q228 -16 456 74V149H0Z" fill="var(--wine)"/>
  </svg>
  <div class="abs" style="left:370px;top:420px;width:70px;height:200px;background:radial-gradient(ellipse,rgba(160,160,160,.15),rgba(160,160,160,0) 70%)" role="img" aria-label="Dezente Besteck-Silhouette als Hintergrundmotiv"></div>

  <p class="abs reserve" style="top:546px;font-size:15px;font-weight:600;letter-spacing:2px">Reservieren Sie gerne unter:</p>
  <p class="abs reserve" style="top:567px;font-size:26px;font-weight:700">05721 / 8640</p>
  <p class="abs reserve" style="top:606px;font-size:11px;font-weight:600;letter-spacing:3.2px">Wir freuen uns darauf, Sie bei uns zu begrüßen!</p>
</section>

</body>
</html>
```